We need a flyer designed for our 4th Annual Harvestlight: A Kinfolk Gathering of Heritage Festival that includes the day, time, location, address, and logos. It also needs to include what to expect. The event will be held on Saturday June 14th from 12p-6p at Gallery Commons located at 418 N. Belcourt Ave., Pensacola, FL 32507. Please see uploaded files for prior flyers for reference when it comes to information to include. Also I've uploaded pictures from our prior festivals that you may incorporate and logos.

```html
<!DOCTYPE html>
<html lang="en">
<head>
<meta charset="utf-8">
<title>4th Annual Harvestlight Festival Flyer</title>
<link href="https://fonts.googleapis.com/css2?family=Anton&family=Oswald:wght@600&family=Poppins:wght@400;500;600;700&family=Mrs+Saint+Delafield&display=swap" rel="stylesheet">
<style>
:root{
  --red:#e31b3b;
  --yellow:#fbbd1e;
  --green:#109457;
  --black:#231f20;
  --paper:#f7f5f2;
  --stage:#d9d9d6;
  --gold:#b8861b;
}
*{box-sizing:border-box;margin:0;padding:0}
html,body{width:1200px;height:710px;overflow:hidden;background:var(--stage)}
.flyer{position:absolute;left:325px;top:0;width:549px;height:710px;background:var(--paper);overflow:hidden;font-family:"Poppins",sans-serif;color:var(--black)}
.border-pattern{position:absolute;top:0;width:48px;height:710px;
  background:linear-gradient(180deg,var(--red) 0 8%,var(--green) 8% 16%,var(--black) 16% 24%,var(--yellow) 24% 32%,var(--red) 32% 40%,var(--black) 40% 48%,var(--green) 48% 56%,var(--yellow) 56% 64%,var(--red) 64% 72%,var(--black) 72% 80%,var(--green) 80% 88%,var(--yellow) 88% 94%,var(--red) 94% 100%)}
.border-left{left:0}
.border-right{right:0;background:linear-gradient(180deg,var(--yellow) 0 6%,var(--green) 6% 14%,var(--black) 14% 22%,var(--red) 22% 30%,var(--yellow) 30% 38%,var(--green) 38% 46%,var(--black) 46% 54%,var(--red) 54% 62%,var(--yellow) 62% 70%,var(--green) 70% 78%,var(--black) 78% 86%,var(--red) 86% 94%,var(--green) 94% 100%)}
.presents{position:absolute;left:83px;width:379px;top:30px;text-align:right;font-size:17px;font-weight:400;letter-spacing:.2px;line-height:1;white-space:nowrap}
.edition{position:absolute;left:83px;width:379px;top:50px;text-align:right;font-size:25px;font-weight:500;color:var(--green);line-height:1;letter-spacing:.2px;white-space:nowrap}
.title{position:absolute;left:82px;top:80px;width:381px;height:94px}
.title text{font-family:"Anton",sans-serif}
.tagline{position:absolute;left:83px;width:379px;top:176px;text-align:center;font-family:"Mrs Saint Delafield",cursive;font-size:36px;line-height:1;white-space:nowrap}
.invite{position:absolute;left:83px;top:211px;width:379px;height:26px;background:var(--green);color:#fff;font-weight:600;font-size:13px;display:flex;align-items:center;justify-content:center;white-space:nowrap}
.details{position:absolute;left:83px;top:253px;width:379px;height:54px}
.tag{position:absolute;top:7px;width:19px;height:40px;background:var(--yellow);display:flex;align-items:center;justify-content:center}
.tag span{transform:rotate(-90deg);font-size:9px;font-weight:500;letter-spacing:.5px}
.date-tag{left:0}
.date-day{position:absolute;left:22px;top:7px;font-size:22px;font-weight:700;line-height:1;white-space:nowrap}
.date-year{position:absolute;left:22px;top:31px;font-size:15px;font-weight:400;line-height:1;white-space:nowrap}
.time{position:absolute;left:165px;top:0;width:56px;height:54px;background:var(--black);color:#fff;font-family:"Oswald",sans-serif;font-weight:600;font-size:14px;line-height:1.2;display:flex;flex-direction:column;align-items:center;justify-content:center}
.time span{white-space:nowrap}
.venue-tag{left:242px}
.venue{position:absolute;left:265px;top:10px;font-size:10.3px;font-weight:500;line-height:1.1;white-space:nowrap}
.expect{position:absolute;left:83px;top:328px;width:379px;height:101px;background:var(--yellow);padding:6px 12px 0 14px}
.expect h2{text-align:center;color:var(--red);font-size:17px;font-weight:700;line-height:1.1;margin-bottom:3px}
.expect ul{list-style:none;display:grid;grid-template-columns:162px 1fr;column-gap:0}
.expect li{font-size:10.6px;font-weight:500;line-height:16px;position:relative;padding-left:10px;white-space:nowrap}
.expect li::before{content:"";position:absolute;left:0;top:5px;width:5px;height:5px;background:var(--red)}
.expect li.continued::before{display:none}
.free{position:absolute;left:83px;top:429px;width:379px;height:26px;background:var(--red);color:#fff;font-weight:700;font-size:15px;letter-spacing:.4px;display:flex;align-items:center;justify-content:center;white-space:nowrap}
.partners{position:absolute;left:83px;top:466px;width:379px;height:32px;display:flex;align-items:center;justify-content:space-between;padding:0 6px 0 14px}
.partner{display:flex;align-items:center;gap:6px;font-size:10.5px;font-weight:600;white-space:nowrap}
.partner-mark{width:14px;height:14px}
.firm{color:var(--gold)}
.firm .partner-mark{background:var(--gold)}
.foundation{color:var(--black)}
.foundation .partner-mark{background:var(--red);border-radius:50%}
.event-photo{position:absolute;left:48px;top:502px;width:453px;height:176px;background:linear-gradient(180deg,#eef0f1 0%,#cfd6d3 38%,#7e7a76 62%,#3b3735 100%)}
.footer{position:absolute;left:48px;top:678px;width:453px;height:32px;background:var(--black);color:#e9e9e9;font-size:12px;letter-spacing:2.4px;display:flex;align-items:center;justify-content:center}
</style>
</head>
<body>
<main class="flyer">
  <div class="border-pattern border-left" role="img" aria-label="Geometric heritage pattern border in red, yellow, green and black"></div>
  <div class="border-pattern border-right" role="img" aria-label="Geometric heritage pattern border in red, yellow, green and black"></div>

  <p class="presents">The Marlow Family Foundation Presents</p>
  <p class="edition">The 4th Annual Harvestlight</p>

  <svg class="title" viewBox="0 0 381 94" aria-label="Harvest Light">
    <defs>
      <linearGradient id="titleFill" x1="0" y1="0" x2="0" y2="1">
        <stop offset="0" stop-color="#f8b51a"/>
        <stop offset=".55" stop-color="#fde9a6"/>
        <stop offset="1" stop-color="#ffffff"/>
      </linearGradient>
    </defs>
    <text x="2" y="89" font-size="100" textLength="377" lengthAdjust="spacingAndGlyphs" fill="url(#titleFill)" stroke="#e31b3b" stroke-width="3" paint-order="stroke">HARVEST LIGHT</text>
  </svg>

  <p class="tagline">A Kinfolk Gathering of Heritage</p>

  <p class="invite">Come &amp; Join Us for a Day of Freedom Celebration!</p>

  <section class="details">
    <div class="tag date-tag"><span>DATE</span></div>
    <p class="date-day">14th JUNE</p>
    <p class="date-year">SATURDAY,2025</p>
    <div class="time"><span>12:00 PM</span><span>6:00 PM</span></div>
    <div class="tag venue-tag"><span>VANUE</span></div>
    <p class="venue">Gallery Commons,<br>418 N. Belcourt Ave.,<br>Pensacola, FL 32507</p>
  </section>

  <section class="expect">
    <h2>WHAT TO EXPECT</h2>
    <ul>
      <li>Live Performances</li>
      <li>African Clothing Vendors</li>
      <li>Food Vendors</li>
      <li>Kids Obstacle Course &amp; Play Area</li>
      <li>Spades &amp; Domino Tables</li>
      <li>Bring Your Own Chairs</li>
      <li>Art &amp; Cultural Exhibits</li>
      <li class="continued">or Picnic Blankets</li>
    </ul>
  </section>
  <p class="free">FREE EVENT – EVERYONE’S WELCOME!</p>

  <section class="partners">
    <div class="partner firm"><span class="partner-mark"></span>Kessler Law Group, PLLC</div>
    <div class="partner foundation"><span class="partner-mark"></span>The Marlow Family Foundation</div>
  </section>

  <div class="event-photo" role="img" aria-label="Photo of performers and guests on the outdoor stage at a prior festival"></div>
  <p class="footer">marlowfamilyfoundation.com</p>
</main>
</body>
</html>
```